Summit Guest Partners

An Editable Business Card Template For SGP & SGH
Similar or Different Design

418 W. Marlow Ridge Pkwy.
Suite 2230
Irving, TX 75038

```html
<!DOCTYPE html>
<html lang="en">
<head>
<meta charset="utf-8">
<title>Summit Guest Partners – Business Cards</title>
<link rel="stylesheet" href="https://fonts.googleapis.com/css2?family=Crimson+Text:wght@400;600&display=swap">
<style>
  :root {
    --bg: #3a3a3a;
    --card: #efefef;
    --card-edge: #dcdcdc;
    --brand-red: #8a2428;
    --brand-red-dark: #761d21;
    --ink: #1f1f1f;
    --white: #ffffff;
  }
  html, body {
    margin: 0;
    width: 1200px;
    height: 1138px;
    overflow: hidden;
    background: var(--bg);
  }
  .stage {
    position: relative;
    width: 1200px;
    height: 1138px;
  }
  .card {
    position: absolute;
    width: 622px;
    height: 377px;
    border-radius: 16px;
    overflow: hidden;
    background: linear-gradient(160deg, var(--white) 0%, var(--card) 55%, var(--card-edge) 100%);
  }
  .card--front { left: 272px; top: 183px; }
  .card--back  { left: 274px; top: 606px; }
  .card svg { display: block; }
  .type { font-family: "Crimson Text", Georgia, serif; }
  .red-fill   { fill: var(--brand-red); }
  .ink-fill   { fill: var(--ink); }
  .white-fill { fill: var(--white); }
  .sc   { font-variant: small-caps; }
  .bold { font-weight: 600; }
</style>
</head>
<body>
<main class="stage">

  <!-- Company card -->
  <section class="card card--front" aria-label="Company card">
    <svg width="622" height="377" viewBox="0 0 622 377" class="type">
      <defs>
        <linearGradient id="header-front" x1="0" y1="0" x2="1" y2="0">
          <stop offset="0" stop-color="var(--brand-red-dark)"/>
          <stop offset="1" stop-color="var(--brand-red)"/>
        </linearGradient>
      </defs>
      <rect class="header-band" x="0" y="0" width="622" height="100" fill="url(#header-front)" role="img" aria-label="Decorative red header band with curved stripes"/>

      <text class="white-fill" x="598" y="52" font-size="24" text-anchor="end">Corporate Office:</text>
      <text class="white-fill bold" x="598" y="85" font-size="30" text-anchor="end">214-555-0148</text>

      <g class="brand-name">
        <circle class="red-fill" cx="80" cy="172" r="15"/>
        <text class="red-fill" x="104" y="188" font-size="46">SGP</text>
        <text class="red-fill" x="172" y="222" font-size="16" text-anchor="middle">Summit Guest Partners</text>
      </g>

      <text class="red-fill" x="747" y="0" font-size="0"></text>
      <text class="red-fill" x="598" y="209" font-size="17" text-anchor="end">Experienced provider to Oil, Gas,</text>
      <text class="red-fill" x="598" y="226" font-size="17" text-anchor="end">Energy &amp; Construction Industries.</text>

      <g class="services" font-size="15.5">
        <text class="ink-fill" x="578" y="255" text-anchor="end">Consolidated Billing</text>
        <text class="ink-fill" x="578" y="278" text-anchor="end">Full Service Corporate Lodging</text>
        <text class="ink-fill" x="578" y="301" text-anchor="end">Live Customer Support 27/7/365</text>
        <text class="ink-fill" x="578" y="324" text-anchor="end">Prover Track Record of Performance</text>
        <text class="ink-fill" x="578" y="347" text-anchor="end">Best Negotiated Rates &amp; No Additional Fees</text>
        <circle class="red-fill" cx="593" cy="250" r="3.5"/>
        <circle class="red-fill" cx="593" cy="273" r="3.5"/>
        <circle class="red-fill" cx="593" cy="296" r="3.5"/>
        <circle class="red-fill" cx="593" cy="319" r="3.5"/>
        <circle class="red-fill" cx="593" cy="342" r="3.5"/>
      </g>

      <g class="address" font-size="16" text-anchor="middle">
        <text class="ink-fill" x="138" y="295">418 W. Marlow Ridge Pkwy.</text>
        <text class="ink-fill" x="138" y="318">Suite 2230 Irving, TX 75038</text>
        <text class="red-fill sc" x="138" y="347" font-size="18.5">www.SGPFieldStay.com</text>
      </g>
    </svg>
  </section>

  <!-- Personal card -->
  <section class="card card--back" aria-label="Personal card">
    <svg width="622" height="377" viewBox="0 0 622 377" class="type">
      <defs>
        <linearGradient id="header-back" x1="0" y1="0" x2="1" y2="0">
          <stop offset="0" stop-color="var(--brand-red-dark)"/>
          <stop offset="1" stop-color="var(--brand-red)"/>
        </linearGradient>
      </defs>
      <rect class="header-band" x="0" y="0" width="622" height="100" fill="url(#header-back)" role="img" aria-label="Decorative red header band with curved stripes"/>

      <text class="white-fill sc" x="591" y="45" font-size="26" text-anchor="end">Oil Field Housing</text>
      <text class="white-fill sc" x="591" y="76" font-size="26" text-anchor="end">on Autopilot</text>

      <g class="brand-name">
        <circle class="red-fill" cx="66" cy="228" r="18"/>
        <text class="red-fill" x="96" y="246" font-size="56">SGH</text>
        <text class="red-fill" x="150" y="282" font-size="18" text-anchor="middle">Summit Guest Housing</text>
      </g>

      <text class="red-fill bold" x="591" y="225" font-size="30" text-anchor="end">Dana Whitcomb</text>
      <text class="ink-fill" x="591" y="248" font-size="19" text-anchor="end">Sales Manager</text>

      <g class="contact" font-size="19">
        <text class="ink-fill" x="564" y="294" text-anchor="end">214-555-0148</text>
        <text class="ink-fill" x="564" y="318" text-anchor="end">480-555-0176</text>
        <text class="ink-fill" x="564" y="342" text-anchor="end">dwhitcomb@summitguest.com</text>
      </g>

      <g class="icon icon--phone" transform="translate(574,280)">
        <path class="red-fill" d="M1,4 C1,1 15,1 15,4 L13,6 L10,5 L10,4 L6,4 L6,5 L3,6 Z"/>
        <rect class="red-fill" x="3" y="7" width="10" height="7" rx="1"/>
      </g>
      <g class="icon icon--mobile" transform="translate(577,303)">
        <rect x="0.8" y="0.8" width="8.4" height="15" rx="1.5" fill="none" stroke="var(--brand-red)" stroke-width="1.6"/>
        <rect class="red-fill" x="3" y="3" width="4" height="8"/>
      </g>
      <g class="icon icon--mail" transform="translate(574,331)">
        <rect class="red-fill" x="0" y="0" width="15" height="11" rx="1"/>
        <path d="M0.5,0.5 L7.5,6.5 L14.5,0.5 M0.5,10.5 L5.5,5 M14.5,10.5 L9.5,5" fill="none" stroke="var(--white)" stroke-width="1.2"/>
      </g>
    </svg>
  </section>

</main>
</body>
</html>
```